New Property management company business cards

Looking for a new business card, to reflect new younger ownership
Card should be clean, simple and professional but with a modern layout that is conveys our new logo and business model

Key aspects of the business:

Property Management
Facility Maintenance
Project Management
Tenant Improvements

Mailing Address:
PO BOX 7816
Fairhaven CA, 95021

Phone: 530-418-6071
Direct: 530-418-6074

Doyle Marsh
President

Target Market(s)

Commercial property owners

Industry/Entity Type

Real Estate property management

Contact Information for Business Card

Open to all designs but lean toward vertical layouts

Requirements
Must have
• Logo and space to customize name and contact info

```html
<!DOCTYPE html>
<html lang="en">
<head>
<meta charset="utf-8">
<title>Valebrook Property Management – Business Card</title>
<link href="https://fonts.googleapis.com/css2?family=Montserrat:wght@400;500;600;700&display=swap" rel="stylesheet">
<style>
  :root {
    --page-bg: #e9e4dc;
    --card-bg: #f4f1ec;
    --card-edge: #ffffff;
    --ink-dark: #2f2f34;
    --ink-mid: #3d3d42;
    --teal: #1f9a7d;
    --band: #36363a;
    --band-text: #d9d6d0;
  }
  * { box-sizing: border-box; margin: 0; padding: 0; }
  html, body {
    width: 1200px;
    height: 1047px;
    overflow: hidden;
    background: var(--page-bg);
    font-family: "Montserrat", sans-serif;
  }
  .canvas { position: relative; width: 1200px; height: 1047px; }
  .business-card {
    position: absolute;
    left: 151px;
    top: 289px;
    width: 947px;
    height: 518px;
    background: var(--card-bg);
    border: 2px solid var(--card-edge);
    border-radius: 24px;
    box-shadow: 0 10px 30px rgba(60, 50, 40, 0.12);
    overflow: hidden;
  }
  .brand-mark {
    position: absolute;
    left: 236px;
    top: 180px;
    width: 40px;
    height: 40px;
    background: var(--teal);
  }
  .brand-name {
    position: absolute;
    left: 288px;
    top: 170px;
    color: var(--ink-dark);
    font-weight: 600;
    white-space: nowrap;
  }
  .brand-name .word {
    display: block;
    font-size: 54px;
    line-height: 60px;
    letter-spacing: 6px;
  }
  .brand-name .line {
    display: block;
    font-size: 15px;
    line-height: 18px;
    letter-spacing: 4.4px;
    margin-top: 2px;
  }
  .person {
    position: absolute;
    right: calc(947px - 453px);
    top: 298px;
    text-align: right;
    white-space: nowrap;
  }
  .person-name {
    color: var(--teal);
    font-size: 33px;
    font-weight: 600;
    line-height: 44px;
  }
  .person-title {
    color: var(--ink-mid);
    font-size: 21px;
    font-weight: 500;
    line-height: 28px;
    margin-top: 2px;
  }
  .divider {
    position: absolute;
    left: 479px;
    top: 306px;
    width: 2px;
    height: 60px;
    background: var(--teal);
  }
  .numbers {
    position: absolute;
    left: 499px;
    top: 305px;
    list-style: none;
  }
  .numbers li {
    display: flex;
    align-items: center;
    gap: 14px;
    color: var(--ink-dark);
    font-size: 21px;
    font-weight: 500;
    height: 33px;
    white-space: nowrap;
  }
  .numbers svg { width: 21px; height: 21px; flex: none; }
  .address-band {
    position: absolute;
    left: 0;
    top: 447px;
    width: 100%;
    height: 31px;
    background: var(--band);
    color: var(--band-text);
    font-size: 21px;
    font-weight: 400;
    line-height: 31px;
    text-align: center;
  }
</style>
</head>
<body>
<main class="canvas">
  <article class="business-card">
    <span class="brand-mark" aria-hidden="true"></span>
    <h1 class="brand-name">
      <span class="word">VALEBROOK</span>
      <span class="line">PROPERTY MANAGEMENT</span>
    </h1>

    <div class="person">
      <p class="person-name">Doyle Marsh</p>
      <p class="person-title">President</p>
    </div>
    <div class="divider" aria-hidden="true"></div>
    <ul class="numbers">
      <li>
        <svg viewBox="0 0 24 24" aria-hidden="true">
          <path fill="var(--teal)" d="M6.6 10.8a15.1 15.1 0 0 0 6.6 6.6l2.2-2.2a1 1 0 0 1 1-.25 11.4 11.4 0 0 0 3.6.57 1 1 0 0 1 1 1V20a1 1 0 0 1-1 1A17 17 0 0 1 3 4a1 1 0 0 1 1-1h3.5a1 1 0 0 1 1 1c0 1.25.2 2.45.57 3.57a1 1 0 0 1-.25 1z"/>
        </svg>
        530-418-6071
      </li>
      <li>
        <svg viewBox="0 0 24 24" aria-hidden="true">
          <path fill="none" stroke="var(--teal)" stroke-width="2" stroke-linejoin="round" d="M21 3 3 10.5l7.5 3L13.5 21z M10.5 13.5 21 3"/>
        </svg>
        530-418-6074
      </li>
    </ul>

    <footer class="address-band">PO BOX 7816 Fairhaven CA, 95021</footer>
  </article>
</main>
</body>
</html>
```